Accountancy Firm A5 flyer Design

We are looking for an eye catching A5 flyer for our firm, it will be sent to SME's therefore it has to look clean, attractive & elegant.

The target audience: SME's, Taxpayers, Companies, Businesses

Highlight this: Specialist Contractor Accountants
Color scheme: Similar to the logo & Website ( www.finvelo.co.uk)
Slogan: Meets your business needs beyond numbers.
Size: A5
Info to be displayed: Logo, Services, why us, Institue logo, Partners logo,
QR code if possible ( small)
Testimonials: https://lnk.example-short.net/Qw7rTz

References: See attached.

https://www.pagemoldix.com/Templates/Flyer/Financial-Services/Accounting-Bookkeeping/Template-Design-Library.aspx
https://www.pagemoldix.com/Templates/Flyer-Ad/Tax-Preparer-Flyer-Ad-Template-Design-KV5829304.aspx

Target Market(s)

SME's, Taxpayers, Companies, Businesses

Industry/Entity Type

Accounting

Font styles to use
Sans Serif

Colors
ffffff
ec1f27

Requirements
Must have
• eye catching, Highlight this: Specialist Contractor Accountants
• Color scheme: Similar to the logo & Website ( www.finvelo.co.uk)
• Slogan: Meets your business needs beyond numbers.
• Size: A5
• Info to be displayed: Logo, Services, why us, Institue logo, Partners logo,
• QR code if possible ( small)
Nice to have
• Testimonials: https://lnk.example-short.net/Qw7rTz
Should not have
• Bad Color Scheme

```html
<!DOCTYPE html>
<html lang="en">
<head>
<meta charset="utf-8">
<title>Finvelo – Friendly Accountants and Tax Consultants</title>
<link rel="stylesheet" href="https://fonts.googleapis.com/css2?family=Open+Sans:ital,wght@0,400;0,600;0,700;1,600&family=Roboto+Condensed:wght@500&display=swap">
<style>
  :root {
    --page-bg: #e6e4e1;
    --paper: #ffffff;
    --ink: #333333;
    --ink-soft: #555555;
    --rule-dark: #4a4a4a;
    --brand-red: #ec1f27;
    --band-red-deep: #a52a2a;
    --band-red: #bd3131;
    --hero-red-1: #d9837a;
    --hero-red-2: #c9675f;
    --frame-grey: #9a9a9a;
    --footer-grey: #d3d5d8;
    --badge-neutral: #d7d7d9;
  }
  * { box-sizing: border-box; margin: 0; padding: 0; }
  html, body { width: 1015px; height: 1200px; overflow: hidden; }
  body { background: var(--page-bg); font-family: "Open Sans", Arial, sans-serif; color: var(--ink); }

  .flyer { position: absolute; left: 84px; top: 0; width: 846px; height: 1200px; background: var(--paper); overflow: hidden; }

  .masthead { position: absolute; left: 0; top: 0; width: 100%; height: 138px; }
  .brand { position: absolute; left: 40px; top: 36px; }
  .brand-name { display: flex; align-items: center; gap: 10px; font-size: 50px; font-weight: 400; letter-spacing: 1px; color: var(--ink); line-height: 1; }
  .brand-mark { width: 16px; height: 16px; background: var(--brand-red); }
  .brand-sub { font-family: "Roboto Condensed", "Arial Narrow", sans-serif; font-weight: 500; font-size: 17px; color: var(--ink); margin-top: 6px; letter-spacing: 0.2px; }
  .slogan { position: absolute; right: 30px; top: 40px; text-align: right; font-style: italic; font-weight: 600; font-size: 24px; line-height: 29px; color: var(--ink-soft); }

  .masthead-rule { position: absolute; left: 0; top: 138px; width: 100%; height: 8px; background: var(--rule-dark); }

  .hero { position: absolute; left: 0; top: 146px; width: 100%; height: 410px;
    background: linear-gradient(120deg, var(--hero-red-2) 0%, var(--hero-red-1) 45%, #e0a39b 75%, var(--hero-red-2) 100%); }
  .hero-title { position: absolute; left: 38px; top: 190px; color: #fff; font-weight: 700; font-size: 43px; line-height: 52px; }
  .hero-intro { position: absolute; left: 38px; top: 298px; width: 340px; color: #fff; font-size: 21.5px; line-height: 26.5px; }

  .panel { position: absolute; top: 465px; width: 386px; height: 541px; background: var(--paper);
    border: 2px solid var(--frame-grey); border-radius: 12px; overflow: hidden; }
  .panel--services { left: 26px; }
  .panel--why { left: 431px; }
  .panel-head { height: 92px; display: flex; align-items: center; justify-content: center; color: #fff; font-size: 36px; font-weight: 400; }
  .panel--services .panel-head { background: var(--band-red-deep); }
  .panel--why .panel-head { background: var(--band-red); }

  .ticklist { list-style: none; }
  .panel--services .ticklist { padding: 24px 0 0 42px; }
  .panel--why .ticklist { padding: 80px 0 0 33px; }
  .ticklist li { display: flex; align-items: center; gap: 10px; font-size: 20.5px; line-height: 28.2px; color: var(--ink-soft); white-space: nowrap; }
  .ticklist svg { width: 17px; height: 17px; flex: none; }

  .partners { position: absolute; left: 0; top: 1030px; width: 100%; height: 60px; }
  .partner { position: absolute; top: 8px; width: 120px; height: 44px; border-radius: 6px; background: var(--badge-neutral); }

  .footer-rule { position: absolute; left: 0; top: 1113px; width: 100%; height: 6px; background: var(--rule-dark); }
  .contact { position: absolute; left: 0; top: 1119px; width: 100%; height: 81px; background: var(--footer-grey);
    display: flex; align-items: center; justify-content: center; gap: 10px; font-size: 18.5px; color: var(--ink-soft); }
  .contact strong { font-weight: 700; color: var(--ink); }
</style>
</head>
<body>
<svg width="0" height="0" style="position:absolute">
  <symbol id="tick-box" viewBox="0 0 18 18">
    <rect x="1.5" y="4" width="12" height="12" rx="2" fill="none" stroke="#c7282e" stroke-width="2"/>
    <path d="M4.5 9.5 L8 13 L16.5 2.5" fill="none" stroke="#c7282e" stroke-width="2.4" stroke-linecap="round" stroke-linejoin="round"/>
  </symbol>
</svg>

<main class="flyer">
  <header class="masthead">
    <div class="brand">
      <div class="brand-name"><span>FINVELO</span><span class="brand-mark"></span></div>
      <div class="brand-sub">ACCOUNTANTS &amp; TAX CONSULTANTS</div>
    </div>
    <p class="slogan">Meets your business needs<br>beyond numbers.</p>
  </header>
  <div class="masthead-rule"></div>

  <section class="hero" role="img" aria-label="Photo of a tax return form, calculator and reading glasses on a desk, tinted red"></section>
  <h1 class="hero-title">Friendly Accountants<br>and Tax Consultants</h1>
  <p class="hero-intro">We are a professional firm of London Accountants who have provided top-notch bookkeeping and taxation services in London for over seven years.</p>

  <section class="panel panel--services">
    <h2 class="panel-head">Our Services:</h2>
    <ul class="ticklist">
      <li><svg><use href="#tick-box"/></svg>Company Formation</li>
      <li><svg><use href="#tick-box"/></svg>Company Accounts</li>
      <li><svg><use href="#tick-box"/></svg>Non Resident Landlord Taxes</li>
      <li><svg><use href="#tick-box"/></svg>Landlords Tax Returns</li>
      <li><svg><use href="#tick-box"/></svg>Tax Investigations</li>
      <li><svg><use href="#tick-box"/></svg>Payroll &amp; PAYE</li>
      <li><svg><use href="#tick-box"/></svg>Bookkeeping</li>
      <li><svg><use href="#tick-box"/></svg>Business Start-up Advice</li>
      <li><svg><use href="#tick-box"/></svg>Company Tax Returns</li>
      <li><svg><use href="#tick-box"/></svg>Personal Tax Returns</li>
      <li><svg><use href="#tick-box"/></svg>C.I.S - Tax Refunds</li>
      <li><svg><use href="#tick-box"/></svg>Tax Planning</li>
      <li><svg><use href="#tick-box"/></svg>Work Place Pension</li>
      <li><svg><use href="#tick-box"/></svg>Registered Office Address</li>
    </ul>
  </section>

  <section class="panel panel--why">
    <h2 class="panel-head">Why Us?</h2>
    <ul class="ticklist">
      <li><svg><use href="#tick-box"/></svg>Qualified &amp; experienced team</li>
      <li><svg><use href="#tick-box"/></svg>Over 40 years of experience</li>
      <li><svg><use href="#tick-box"/></svg>Monthly Newsletters &amp; tax tips</li>
      <li><svg><use href="#tick-box"/></svg>Free telephone &amp; email support</li>
      <li><svg><use href="#tick-box"/></svg>Never miss any deadline*</li>
      <li><svg><use href="#tick-box"/></svg>Fixed Fees – No surprise bills</li>
      <li><svg><use href="#tick-box"/></svg>Dedicated accounts manage</li>
      <li><svg><use href="#tick-box"/></svg>Work on time, Every Time</li>
      <li><svg><use href="#tick-box"/></svg>Guaranteed Satisfaction</li>
      <li><svg><use href="#tick-box"/></svg>Excellent Customer Service</li>
    </ul>
  </section>

  <div class="partners">
    <div class="partner" style="left:66px" role="img" aria-label="Accounting body membership badge"></div>
    <div class="partner" style="left:256px" role="img" aria-label="Chartered accountants institute badge"></div>
    <div class="partner" style="left:455px" role="img" aria-label="Workplace pension partner badge"></div>
    <div class="partner" style="left:637px" role="img" aria-label="Accounting software partner badge"></div>
  </div>

  <div class="footer-rule"></div>
  <footer class="contact">
    <span>48 Harrow Lane, Merton, SM9 2XT</span>
    <span>Phone: <strong>0203 5510 947</strong></span>
    <span>Website: <strong>www.finvelo.co.uk</strong></span>
  </footer>
</main>
</body>
</html>
```